Specialized Personal Trainer Needs a Business Card Design

I need a business card design for my personal training business called Tall Oak Fitness. I have my Human Kinetics degree in Exercise Science from the Halvern Ridge University as well as an extra certification from NBEP (National Board of Exercise Practice). I work as a Cardiac Rehab Exercise Specialist and personal trainer giving specialized exercise prescriptions to those that have different heart conditions as well as work with the general population in weight loss, strength and conditioning, getting/staying fit.
Updates

I decided that I wanted a logo (as I did not have one before I submitted my project for a business card) so I am submitting a project to get a logo done and then I will decide on a business card, hopefully being able to use one of the designs already submitted.  My apologies for doing this backwards.  I am new to this so I appreciate your patience.

Thank you.

Hi, I have just created a project for a logo design (I realized I needed a logo and I should've done that first..oops!), please feel free to participate.  Once I receive a logo I like I will finalize my business card project and hopefully incorporate it into one of your business card designs. 

Thank you!

Target Market(s)

Business professionals

Industry/Entity Type

Personal Trainer

Requirements
Must have
• My name with my info:
Celia R. Dunhill (BHK)
NBEP Certified Clinical Exercise Specialist & Personal Trainer
celia.dunhill@talloakfitness.example
Cell: 604-358-4170

Please make it double sided.
Nice to have
• An image that represents cardiac and general fitness training.

```html
<!DOCTYPE html>
<html lang="en">
<head>
<meta charset="utf-8">
<title>Celia R. Dunhill – Business Card</title>
<link rel="stylesheet" href="https://fonts.googleapis.com/css2?family=Source+Sans+3:ital,wght@0,400;0,600;0,700;1,400&display=swap">
<style>
  :root {
    --ink: #000000;
    --paper: #ffffff;
    --silver-text: #c4c4c4;
    --grey-dark: #5a5a5a;
    --grey-mid: #8c8c8c;
    --grey-light: #d8d8d8;
    --pattern-tone: #ececec;
    --band-tone: #dcdcdc;
    --accent-red: #e3000f;
  }
  * { box-sizing: border-box; margin: 0; padding: 0; }
  html, body { width: 1200px; height: 974px; overflow: hidden; background: var(--paper); }
  body { position: relative; font-family: "Source Sans 3", sans-serif; }

  .card {
    position: absolute;
    left: 241px;
    width: 716px;
    height: 397px;
    box-shadow: 0 14px 22px rgba(0,0,0,0.35);
    overflow: hidden;
  }
  .card--front { top: 60px; }
  .card--back { top: 494px; background: var(--paper); }

  .card__art { position: absolute; inset: 0; width: 100%; height: 100%; }

  .name {
    position: absolute;
    font-weight: 600;
    font-size: 36px;
    line-height: 1;
    white-space: nowrap;
  }
  .title {
    position: absolute;
    font-style: italic;
    font-size: 16px;
    line-height: 1;
    white-space: nowrap;
  }
  .contact {
    position: absolute;
    line-height: 1;
    white-space: nowrap;
  }

  /* Front */
  .card--front .name { left: 40px; top: 40px; color: var(--silver-text); }
  .card--front .title { left: 40px; top: 88px; color: var(--silver-text); }
  .card--front .contact { left: 114px; color: var(--paper); }
  .card--front .contact--phone { top: 196px; font-size: 35px; }
  .card--front .contact--email { top: 277px; font-size: 22px; }

  .brand {
    position: absolute;
    display: flex;
    align-items: center;
    gap: 10px;
    font-weight: 700;
    white-space: nowrap;
  }
  .brand__dot { display: block; border-radius: 50%; background: var(--ink); }
  .card--front .brand { right: 20px; bottom: 40px; font-size: 19px; color: var(--ink); }
  .card--front .brand__dot { width: 30px; height: 30px; }

  /* Back */
  .back-texture {
    position: absolute; left: 0; top: 0; width: 716px; height: 361px;
    background: linear-gradient(180deg, #f1f1f1, var(--pattern-tone));
  }
  .back-band { position: absolute; left: 0; top: 361px; width: 716px; height: 15px; background: var(--band-tone); }
  .back-rule { position: absolute; left: 0; top: 376px; width: 716px; height: 4px; background: var(--ink); }

  .card--back .brand { left: 0; width: 716px; top: 58px; justify-content: center; font-size: 26px; color: var(--ink); }
  .card--back .brand__dot { width: 46px; height: 46px; background: var(--grey-mid); }
  .card--back .name { left: 121px; top: 142px; color: var(--ink); }
  .card--back .title { left: 121px; top: 184px; color: var(--ink); }
  .card--back .contact { left: 199px; font-size: 22px; color: var(--ink); }
  .card--back .contact--phone { top: 248px; }
  .card--back .contact--email { top: 294px; }
  .back-icons { position: absolute; left: 0; top: 0; width: 716px; height: 397px; }
</style>
</head>
<body>

<section class="card card--front" aria-label="Business card front">
  <svg class="card__art" viewBox="0 0 716 397" aria-hidden="true">
    <defs>
      <linearGradient id="frame-fade" x1="0" y1="0" x2="1" y2="1">
        <stop offset="0" stop-color="#7a7a7a"/>
        <stop offset="0.55" stop-color="#8e8e8e"/>
        <stop offset="1" stop-color="#cfcfcf"/>
      </linearGradient>
      <linearGradient id="edge-fade" x1="0" y1="0" x2="1" y2="0">
        <stop offset="0" stop-color="#ffffff" stop-opacity="0.25"/>
        <stop offset="1" stop-color="#000000" stop-opacity="0"/>
      </linearGradient>
    </defs>
    <rect width="716" height="397" fill="url(#frame-fade)"/>
    <rect x="0" y="0" width="20" height="397" fill="url(#edge-fade)"/>
    <path d="M20 17 H716 V40 C680 240 500 380 262 397 H20 Z" fill="#000"/>
    <!-- phone icon -->
    <circle cx="68" cy="214" r="29" fill="#fff"/>
    <rect x="56" y="196" width="24" height="36" rx="4" fill="var(--accent-red)"/>
    <rect x="60" y="201" width="16" height="24" fill="#fff"/>
    <circle cx="68" cy="228.5" r="1.8" fill="#fff"/>
    <!-- mail icon -->
    <circle cx="68" cy="289" r="29" fill="#fff"/>
    <rect x="50" y="277" width="36" height="24" fill="var(--accent-red)"/>
    <path d="M50 277 L68 292 L86 277" fill="none" stroke="#fff" stroke-width="2.5"/>
  </svg>
  <h1 class="name">Celia R. Dunhill (BHK)</h1>
  <p class="title">NBEP Certified Clinical Exercise Specialist &amp; Personal Trainer</p>
  <p class="contact contact--phone">604-358-4170</p>
  <p class="contact contact--email">celia.dunhill@talloakfitness.example</p>
  <div class="brand"><span class="brand__dot"></span>Tall Oak Fitness</div>
</section>

<section class="card card--back" aria-label="Business card back">
  <div class="back-texture" role="img" aria-label="Faint repeating heart pattern background"></div>
  <div class="back-band"></div>
  <div class="back-rule"></div>
  <div class="brand"><span class="brand__dot"></span>Tall Oak Fitness</div>
  <h2 class="name">Celia R. Dunhill (BHK)</h2>
  <p class="title">NBEP Certified Clinical Exercise Specialist &amp; Personal Trainer</p>
  <svg class="back-icons" viewBox="0 0 716 397" aria-hidden="true">
    <circle cx="139" cy="259" r="17" fill="#000"/>
    <rect x="132" y="249" width="14" height="20" rx="2.5" fill="#fff"/>
    <rect x="134.5" y="252" width="9" height="13" fill="#000"/>
    <circle cx="139" cy="305" r="17" fill="#000"/>
    <rect x="129" y="298" width="20" height="14" fill="#fff"/>
    <path d="M129 298 L139 306 L149 298" fill="none" stroke="#000" stroke-width="1.6"/>
  </svg>
  <p class="contact contact--phone">604-358-4170</p>
  <p class="contact contact--email">celia.dunhill@talloakfitness.example</p>
</section>

</body>
</html>
```